Five Quill Voices, "Drafting and Polishing Made Bright"

We need a brochure that provides background about our company, identifies our products and services and provides our contact information. If possible, We would like the designer to use an Office suite product such as Word or Publisher to create the brochure if possible. We would like photos, color, something that inspires customers to use our services. We have attached a copy of a draft brochure and we believe the text in the brochure is good, but the brochure is cold, bland and lacks color, style and a fresh quality. We would like all text in the brochure to be included as well as the attached logo and company name somewhere on the front and back of the brochure. Please feel free to resize the logo and use creative license to develop the brochure as you please. However, the brochure colors should compliment the dark blue, light blue and black colors in the logo. Most of all, the brochure needs to be engaging, inviting, fresh and ultra professional. Thanks!

Target Market(s)

Small and large scale businesses who would use self-help books, writing services for blogs and Social Media posts, newsletters and manuscript reviews.

Industry/Entity Type

Marketing

Font styles to use
Serif

Colors
0655a3
3377b5
85acd3
000000

Requirements
Must have
• -Logo and company name; text in draft brochure
• -Color and business photos which relate to the products/services provided
• -Inspiring, engaging, professional feel and style
• -I would like colors which compliment the logo colors (perhaps the colors below, but we are open to designer choices
• -Since this is a writing/editing business, something in the brochure that reflects that would be good.
Nice to have
• -Open; depends on the designer preference
• -Use of Office Word or Publisher program, but we are open to the use of other programs.
Should not have
• -Bland brochure with only text

```html
<!DOCTYPE html>
<html lang="en">
<head>
<meta charset="utf-8">
<title>Five Quill Voices — Brochure</title>
<link href="https://fonts.googleapis.com/css2?family=Noto+Serif:ital,wght@0,400;0,700;1,400&family=Alfa+Slab+One&display=swap" rel="stylesheet">
<style>
:root{
  --navy:#0655a3;
  --mid:#3377b5;
  --light:#85acd3;
  --ink:#000000;
  --head:#1f5fa8;
  --deep:#1a3f9e;
  --paper:#ffffff;
  --teal:#1f8a9a;
}
*{margin:0;padding:0;box-sizing:border-box}
html,body{width:838px;height:1200px;overflow:hidden;background:var(--paper)}
body{position:relative;font-family:"Noto Serif",serif;color:var(--ink)}
.sheet{position:absolute;left:0;width:838px;height:592px;overflow:hidden;border:1.5px solid #222;border-left-width:2px;
  background:linear-gradient(180deg,#dfe9f5 0%,#f4f8fc 55%,#ffffff 100%)}
.sheet--outside{top:0}
.sheet--inside{top:606px;height:594px}
.photo{position:absolute}
.photo--outside{left:0;top:0;width:562px;height:360px;
  background:linear-gradient(180deg,#8fb0d8 0%,#b8cde8 45%,rgba(230,238,248,0) 100%)}
.photo--cover{left:562px;top:0;width:276px;height:220px;
  background:linear-gradient(160deg,#0f5c6e 0%,#2aa0b2 45%,#8fd3e0 100%)}
.photo--inside{left:0;top:0;width:838px;height:300px;
  background:linear-gradient(180deg,#2e5f86 0%,#5f98b8 40%,#b9d3e6 80%,rgba(240,245,250,0) 100%)}
.shapes{position:absolute;left:0;top:0}
.panel{position:absolute;background:var(--paper);font-size:10.2px;line-height:12.7px}
.panel h2{font-size:14px;line-height:16px;font-weight:700;color:var(--head);margin-bottom:1px}
.panel p{margin-bottom:12px}
.note{font-style:italic;color:var(--head)}
.title-ref{font-style:italic;color:var(--head)}
.panel--services{left:23px;top:187px;width:234px;height:375px;padding:13px 14px 0 13px}
.panel--contact{left:299px;top:187px;width:243px;height:333px;text-align:center;font-size:13.2px;line-height:16.5px}
.brand{display:flex;align-items:center;justify-content:center;gap:8px;font-weight:400;color:var(--ink)}
.brand__mark{width:22px;height:22px;background:var(--navy)}
.panel--contact .brand{margin-top:58px;font-size:17px}
.contact__name{margin-top:58px;font-size:17px;color:var(--deep)}
.contact__lines{margin-top:22px}
.contact__lines p{margin-bottom:16px}
.cover{position:absolute;left:562px;top:360px;width:276px;text-align:center}
.cover .brand{font-size:15px;color:var(--ink)}
.tagline{margin-top:40px;font-family:"Alfa Slab One",serif;font-size:13.5px;letter-spacing:.3px;color:var(--deep);text-transform:uppercase}
.panel--overview{left:23px;top:130px;width:233px;height:435px;padding:12px 6px 0 7px}
.panel--products{left:301px;top:130px;width:234px;height:435px;padding:12px 6px 0 8px}
.panel--papers{left:584px;top:130px;width:233px;height:350px;padding:12px 8px 0 7px}
.values{list-style:none}
.values li{position:relative;padding-left:34px;margin-bottom:0}
.values li::before{content:"\2666";position:absolute;left:0;color:var(--navy);font-size:9px}
</style>
</head>
<body>

<section class="sheet sheet--outside">
  <div class="photo photo--outside" role="img" aria-label="Abstract blue digital network photo with world map and binary code"></div>
  <div class="photo photo--cover" role="img" aria-label="Teal digital globe and data grid photo"></div>
  <svg class="shapes" width="838" height="592" viewBox="0 0 838 592" aria-hidden="true">
    <polygon points="0,140 130,250 0,320" fill="#3377b5" opacity=".85"/>
    <polygon points="160,0 556,0 358,190" fill="#0655a3" opacity=".9"/>
    <polygon points="230,0 480,0 358,120" fill="#3377b5" opacity=".7"/>
    <polygon points="0,380 220,592 0,592" fill="#85acd3" opacity=".55"/>
    <polygon points="330,592 556,420 556,592" fill="#3377b5" opacity=".45"/>
    <polygon points="562,175 838,175 700,300" fill="#3377b5" opacity=".85"/>
    <polygon points="562,175 700,300 562,380" fill="#85acd3" opacity=".8"/>
    <polygon points="838,175 700,300 838,380" fill="#85acd3" opacity=".8"/>
    <polygon points="838,100 838,175 760,175" fill="#0655a3" opacity=".8"/>
    <polygon points="565,592 625,540 685,592" fill="#85acd3"/>
    <polygon points="650,592 705,540 760,592" fill="#c3d6ea"/>
    <polygon points="730,592 785,540 838,592" fill="#5a9be0"/>
  </svg>

  <div class="panel panel--services">
    <h2>Newsletters</h2>
    <p>Email newsletters allow you to keep current and prospective customers informed about your brand and engaged with your product and service offerings. Newsletters represent an ideal path to identify target audiences and maintain open lines of communication to encourage prospective sales/services.</p>
    <h2>Manuscript reviews</h2>
    <p>As published writers, we understand the value of reviews and we see reviews as a collaborative process that allows manuscripts to be evaluated and commented upon by experts within the same field of research. The evaluation and critique generated from the review provides authors with feedback to improve their work and allows editors to assess the manuscript suitability for publication.</p>
    <p class="note">Contact us for a free consultation with one of our seasoned staff of writers and/or editors to help guide you along the path to success!</p>
  </div>

  <div class="panel panel--contact">
    <div class="brand"><span class="brand__mark"></span><span>Five Quill Voices</span></div>
    <p class="contact__name">Five Quill Voices</p>
    <div class="contact__lines">
      <p>480 Larkspur Lane, #20417<br>Brookhaven, OR 97402</p>
      <p>541/555-0193</p>
      <p>hello@fivequillvoices.com</p>
    </div>
  </div>

  <div class="cover">
    <div class="brand"><span class="brand__mark"></span><span>Five Quill Voices</span></div>
    <p class="tagline">Drafting and Polishing Made Bright</p>
  </div>
</section>

<section class="sheet sheet--inside">
  <div class="photo photo--inside" role="img" aria-label="Abstract blue and teal digital network photo with world map"></div>
  <svg class="shapes" width="838" height="594" viewBox="0 0 838 594" aria-hidden="true">
    <polygon points="0,0 180,0 0,110" fill="#3377b5" opacity=".8"/>
    <polygon points="140,60 560,60 350,260" fill="#0655a3" opacity=".75"/>
    <polygon points="520,20 838,20 838,230" fill="#3377b5" opacity=".55"/>
    <polygon points="0,594 0,300 180,594" fill="#3377b5" opacity=".55"/>
    <polygon points="560,594 838,340 838,594" fill="#0655a3" opacity=".75"/>
    <polygon points="300,594 420,470 540,594" fill="#85acd3" opacity=".6"/>
  </svg>

  <div class="panel panel--overview">
    <h2>Company Overview Description</h2>
    <p>Five Quill Voices Publications dba Five Quill Voices was founded in 2017 by Maren T. Ellison, a Social Services Administrator, author and publisher. Five Quill Voices has become a trusted name with a solid, local reputation as a small business that offers adult, trade books which focus on improving the financial and physical health of mature adults. Five Quill Voices also provides a multi-disciplinary approach to editing and writing services related to trending topics, educational, evergreen pieces or social media matters.</p>
    <p>Since early 2018, Five Quill Voices's operations have focused on producing scalable, high-quality content solutions to meet unique business to develop content to engage audiences. At Five Quill Voices, we implemented sound organizational goals which center around our values:</p>
    <ul class="values">
      <li>Easy order interface complimented by excellent customer service levels.</li>
      <li>Qualified writers which provide expert editing and writing services.</li>
      <li>Engagement of targeted audiences designed to increase sales and enhance client work product.</li>
      <li>Timely deliverables with 100% satisfaction</li>
    </ul>
  </div>

  <div class="panel panel--products">
    <h2>Our Products &amp; Services</h2>
    <p>Five Quill Voices offers a highly-focused service approach to provide adult, trade books and offer quality editing and writing services to produce blog and social media posts, white papers, newsletters and manuscript reviews.</p>
    <h2>Adult Trade Books</h2>
    <p>We are developing a series of books that will aid Baby Boomers and the Generation X population to develop and maintain good, financial planning practices and maintain stable emotional and physical health while aging. The first book in the series, Wealth, Wellness and Wisdom will be released in the Summer of 2018. <span class="title-ref">Wealth, Wellness and Wisdom</span> is a step-by-step guide to aging in America which includes estate planning, wills and trusts, caregiving, senior housing, and coping with the loss of a loved one.</p>
    <h2>Blog and Social Media Posts</h2>
    <p>Blog posts are used to increase brand awareness in search engines and attract new website visitors with relevant, valuable content.</p>
    <p>With client guidance, writers begin by mapping out each blog post to ensure topics, titles, keywords and formatting</p>
  </div>

  <div class="panel panel--papers">
    <p>engage targeted audiences and support your business’ commercial goals.</p>
    <p>A standard blog post (which is 550 to 650 words) may be designed to devote special attention to a topic. Blog posts are short but are still detailed enough to be mobile and reader-friendly. Further, standard blog posts with navigational aids such as numbered lists, bullet points and headers, can be informative and engaging.</p>
    <h2>White Papers</h2>
    <p>White papers are essential to establishing a brand as a trustworthy leader in a specific industry. These high-quality content papers build credibility among online audiences by demonstrating expertise and offering good lead generation opportunities through downloads from potential customers. Five Quill Voices will work with you to determine the topics that resonate most with your target audience to develop valuable, relevant content that supports business goals.</p>
  </div>
</section>

</body>
</html>
```